Obrelo Business Card

Need a double sided business card. Would like the business card to have the logo on one side and the employees details and business contact details on the other.

Business

```html
<!DOCTYPE html>
<html lang="en">
<head>
<meta charset="utf-8">
<title>Obrelo Business Card</title>
<link rel="stylesheet" href="https://fonts.googleapis.com/css2?family=Quicksand:wght@400;500;600;700&display=swap">
<style>
  :root {
    --backdrop: #ebebea;
    --card-white: #ffffff;
    --brand-green: #9fcc45;
    --ink-dark: #1f1f1f;
    --ink-grey: #666666;
    --card-shadow: rgba(0, 0, 0, 0.16);
  }
  * { margin: 0; padding: 0; box-sizing: border-box; }
  html, body {
    width: 1200px;
    height: 676px;
    overflow: hidden;
    background: var(--backdrop);
    font-family: "Quicksand", sans-serif;
  }
  .card-sheet {
    position: relative;
    width: 1200px;
    height: 676px;
  }
  .card {
    position: absolute;
    top: 75px;
    width: 300px;
    height: 525px;
    box-shadow: 0 6px 22px var(--card-shadow);
  }
  .card--front {
    left: 250px;
    background: var(--card-white);
  }
  .card--back {
    left: 650px;
    background: var(--brand-green);
  }

  /* Front side */
  .front-header {
    position: absolute;
    top: 30px;
    left: 26px;
    right: 26px;
    display: flex;
    justify-content: space-between;
    align-items: center;
  }
  .wordmark {
    display: flex;
    align-items: center;
    gap: 5px;
    font-weight: 600;
    line-height: 1;
  }
  .wordmark-square {
    display: inline-block;
    background: currentColor;
  }
  .wordmark--small {
    color: var(--brand-green);
    font-size: 22px;
  }
  .wordmark--small .wordmark-square {
    width: 10px;
    height: 10px;
  }
  .website {
    font-size: 13px;
    font-weight: 700;
    color: var(--ink-dark);
    letter-spacing: 0.3px;
  }
  .contact-block {
    position: absolute;
    right: 26px;
    bottom: 60px;
    text-align: right;
  }
  .person-name {
    font-size: 27px;
    font-weight: 500;
    color: var(--ink-dark);
    letter-spacing: 1px;
    text-transform: uppercase;
    margin-bottom: 8px;
  }
  .person-role,
  .person-phone,
  .person-email {
    font-size: 13.5px;
    font-weight: 600;
    line-height: 1.6;
  }
  .person-role { color: var(--ink-grey); }
  .person-phone,
  .person-email { color: var(--ink-dark); }

  /* Back side */
  .wordmark--large {
    position: absolute;
    top: 38px;
    left: 32px;
    color: var(--card-white);
    font-size: 64px;
    gap: 10px;
  }
  .wordmark--large .wordmark-square {
    width: 26px;
    height: 26px;
  }
  .website--back {
    position: absolute;
    right: 26px;
    bottom: 32px;
    color: var(--card-white);
    font-weight: 600;
  }
</style>
</head>
<body>
  <main class="card-sheet">
    <section class="card card--front" aria-label="Business card front">
      <header class="front-header">
        <div class="wordmark wordmark--small">
          <span class="wordmark-text">obrelo</span>
          <span class="wordmark-square"></span>
        </div>
        <span class="website">www.obrelo.com</span>
      </header>
      <div class="contact-block">
        <p class="person-name">Daniel Hart</p>
        <p class="person-role">Executive Marketing</p>
        <p class="person-phone">555-014-226</p>
        <p class="person-email">daniel@obrelo.com</p>
      </div>
    </section>

    <section class="card card--back" aria-label="Business card back">
      <div class="wordmark wordmark--large">
        <span class="wordmark-text">obrelo</span>
        <span class="wordmark-square"></span>
      </div>
      <span class="website website--back">www.obrelo.com</span>
    </section>
  </main>
</body>
</html>
```